Rusty Lantern Bar & Grill Takeout Menu

Please create a takeout menu using the attached dine-in menu.
Take out menu size: Tri-Fold 11x17

Industry/Entity Type

Bar & Grill (Restaurant)

Colors

Designer to choose colors to be used in the design.

Requirements
Must have
• Phone number and website. "Order Online" "Order for Delivery"
Nice to have
• Area on the back of the menu to feature happy hour specials.

```html
<!DOCTYPE html>
<html lang="en">
<head>
<meta charset="utf-8">
<title>Rusty Lantern Bar &amp; Grill – Takeout Menu</title>
<link href="https://fonts.googleapis.com/css2?family=Federant&family=Josefin+Sans:wght@400;600;700&family=Titan+One&display=swap" rel="stylesheet">
<style>
:root{
  --page:#ececec;
  --paper:#ffffff;
  --paper-grey:#dcdcdc;
  --ink:#1d1d1d;
  --muted:#444;
  --red:#d3342c;
  --yellow:#e9e85a;
  --art-red:#d9442e;
  --art-warm:#e08a3a;
  --art-blue:#5b79c8;
}
*{box-sizing:border-box;margin:0;padding:0}
html,body{width:851px;height:1200px;overflow:hidden;background:var(--page)}
body{font-family:'Josefin Sans',sans-serif;color:var(--ink);position:relative}
.sheet{position:absolute;left:25px;width:800px;height:510px;display:flex;box-shadow:0 6px 18px rgba(0,0,0,.18)}
.sheet--outside{top:45px}
.sheet--inside{top:645px}
.panel{width:33.333%;height:100%;position:relative;padding:18px 14px;background:var(--paper);overflow:hidden}
.panel--menu{display:flex;flex-direction:column;justify-content:space-between}
.panel--grey{background:var(--paper-grey)}
.panel--yellow{background:var(--yellow);padding:0;display:flex;flex-direction:column}
h2{font-family:'Federant',serif;font-weight:400;font-size:13px;letter-spacing:.5px;margin:2px 0 3px}
h3{font-size:7.4px;font-weight:700;text-decoration:underline;margin:4px 0 2px;letter-spacing:.3px}
.item{margin-bottom:2px}
.row{display:flex;align-items:baseline;font-size:7px;color:var(--red);font-weight:600;line-height:1.3}
.row .dots{flex:1;border-bottom:1px dotted var(--red);margin:0 2px;transform:translateY(-2px)}
.desc{font-size:5.7px;line-height:1.35;color:var(--muted)}
.note{font-size:5.8px;text-align:center;margin:2px 0;line-height:1.4}
.center{text-align:center}
.warn{font-family:'Federant',serif;font-size:5.6px;color:var(--red);text-align:center;font-style:italic;line-height:1.4}
.hh-box{border:1.5px solid var(--red);height:100%;display:flex;flex-direction:column}
.art{display:block}
.art--bar{height:160px;background:linear-gradient(160deg,var(--art-red),#c7382a 60%,#b95a3a)}
.hh{flex:1;text-align:center;display:flex;flex-direction:column;justify-content:space-evenly;padding:6px 0 8px}
.hh-title{font-family:'Federant',serif;color:var(--red);font-size:20px;letter-spacing:1px}
.hh-day{font-family:'Titan One',sans-serif;font-size:12px}
.hh-time{font-size:13px}
.hh-off{font-family:'Titan One',sans-serif;color:var(--red);font-size:29px;line-height:1}
.hh-what{font-size:12px}
.brand{flex:1;display:flex;flex-direction:column;align-items:center;justify-content:center;text-align:center;padding-top:20px}
.brand-name{font-family:'Federant',serif;font-size:34px;line-height:1.05;color:var(--ink)}
.brand-sub{font-family:'Federant',serif;font-size:20px;margin-top:6px}
.order{margin-top:36px;font-family:'Titan One',sans-serif;font-size:11px;line-height:1.5}
.order .phone{font-size:18px}
.art--diners{height:140px;background:linear-gradient(170deg,var(--art-warm),#d9593a 50%,var(--art-blue))}
.frame{border:2.5px dotted var(--ink);border-radius:12px;padding:8px 10px}
.panel--grey .frame{height:100%;display:flex;flex-direction:column;justify-content:space-between}
.group{display:flex;flex-direction:column}
.tiny-logo{text-align:center;font-family:'Federant',serif;font-size:26px;line-height:1.05;margin-top:8px}
.tiny-logo small{display:block;font-size:14px;margin-top:3px}
.intro{font-size:5.8px;line-height:1.45;text-align:center;color:var(--muted);margin-top:3px}
.rule{height:8px;border-bottom:1px solid var(--ink);border-radius:0 0 40% 40%;margin:6px 8px}
.burgers{width:100%;border-collapse:collapse;font-size:6px}
.burgers th{font-family:'Federant',serif;font-weight:400;font-size:6px;text-align:left;padding-bottom:4px}
.burgers td{vertical-align:top;padding-bottom:9px}
.burgers .name{color:var(--red);font-weight:600;font-size:6.6px}
.burgers .price{color:var(--red);width:32px;font-weight:600}
.icon{display:inline-block;width:10px;height:10px;border:1.2px solid var(--ink);border-radius:50%}
.box-title{font-family:'Federant',serif;font-size:12px;text-align:center}
.handhelds{display:grid;grid-template-columns:1fr 1fr;gap:4px 10px;margin-top:4px}
.hh-item .name{display:flex;justify-content:space-between;color:var(--red);font-size:5.8px;font-weight:600}
.extras{display:grid;grid-template-columns:1fr 1fr 1fr;gap:6px;margin-top:10px}
.extras h4{font-family:'Federant',serif;font-weight:400;font-size:8.5px}
.extras p{font-size:4.8px;line-height:1.35;color:var(--muted)}
</style>
</head>
<body>

<section class="sheet sheet--outside">
  <div class="panel panel--menu">
    <h2>SALADS</h2>
    <div class="item"><div class="row">Combo Lantern<span class="dots"></span>11</div><p class="desc">Enjoy a side House and a cup of any soup.</p></div>
    <div class="item"><div class="row">Lantern House Salad<span class="dots"></span>11</div><p class="desc">Spring lettuce mix, fresh red peppers, onion, cherry tomatoes, cucumber and croutons. Served with Red Wine Vinaigrette.</p></div>
    <div class="item"><div class="row">Grilled Chicken Salad<span class="dots"></span>15</div><p class="desc">Spring lettuce mix, grilled chicken breast, bacon, fresh red peppers, onions, tomatoes, cucumber and feta cheese. Served with Red Wine Vinaigrette.</p></div>
    <div class="item"><div class="row">Grilled Shrimp Salad*<span class="dots"></span>16</div><p class="desc">Spring lettuce mix, garlic Roasted Shrimp, roasted corn, pico de gallo fresh avocado. Served with Lemon Champagne Vinaigrette.</p></div>
    <div class="item"><div class="row">Goat Cheese Salad<span class="dots"></span>16</div><p class="desc">Spring lettuce mix, fried goat cheese, fresh red peppers, cranberries, white onions, and cherry tomatoes. Served with Lemon Champagne Vinaigrette.</p></div>
    <div class="item"><div class="row">The Skinny Wick<span class="dots"></span>14</div><p class="desc">Spring lettuce mix, sliced apple, sun dried cranberries, roasted corn, cherry tomatoes, and feta cheese. Served with Balsamic Vinaigrette.</p></div>
    <div class="item"><div class="row">Small House Salad<span class="dots"></span>6</div></div>
    <p class="note"><b>Add:</b> Grilled Chicken 5 | Garlic Roasted Shrimp 5 | Fried Goat Cheese 4</p>
    <p class="note"><b><u>DRESSINGS</u></b><br>Balsamic Vinaigrette | Caesar<br>Red Wine Vinaigrette | Honey-Mustard | Lemon Champagne Vinaigrette |<br>Ranch | Blue Cheese</p>
    <h2>SOUPS &amp; BOWLS</h2>
    <div class="item"><div class="row">Rusty Lantern Chili<span class="dots"></span>Cup 6 | Bowl 8</div><p class="desc">Our Signature Chili with lean ground beef, black beans, and corn. Topped with cheddar cheese and green onion, served with tri-color tortilla chips.</p></div>
    <div class="item"><div class="row">Southwestern Sweet Potato Soup<span class="dots"></span>Cup 6 | Bowl 8</div><p class="desc">A delicious mix of sweet potatoes, corn, bell peppers, and black beans, this vegan soup delivers top flavor and quality with every bowl. Served with tri-color tortilla chips.</p></div>
    <div class="item"><div class="row">Ancient Grains Bowl<span class="dots"></span>12</div><p class="desc">Quinoa, brown rice, kale and fresh spinach, with fire roasted portobello mushrooms, zucchini and red peppers. Topped with fresh avocado, and feta cheese. Served with Lemon Champagne Vinaigrette.</p></div>
    <p class="note"><b>Add:</b> Grilled Chicken 5 | Garlic Roasted Shrimp 5</p>
    <p class="warn">*The consumption of raw or undercooked eggs, meat, poultry, seafood or shellfish<br>may contribute to food borne illness, especially if you have a medical condition.<br>V - Vegetarian · Spicy</p>
  </div>

  <div class="panel">
    <div class="hh-box">
      <div class="art art--bar" role="img" aria-label="Painted illustration of cartoon animal friends drinking at a bar counter"></div>
      <div class="hh">
        <div class="hh-title">HAPPY HOUR</div>
        <div><div class="hh-day">WEDNESDAY - FRIDAY</div><div class="hh-time">5:00 PM to 7:00 PM</div></div>
        <div><div class="hh-day">WEDNESDAY</div><div class="hh-off">$2.00 OFF</div><div class="hh-what">Wine &amp; Draft Beer</div></div>
        <div><div class="hh-day">THURSDAY &amp; FRIDAY</div><div class="hh-off">$2.00 OFF</div><div class="hh-what">Wine &amp; Draft Beer</div><div class="hh-off" style="margin-top:4px">$4.00 OFF</div><div class="hh-what">Cocktails</div></div>
      </div>
    </div>
  </div>

  <div class="panel panel--yellow">
    <div class="brand">
      <div class="brand-name">Rusty<br>Lantern</div>
      <div class="brand-sub">Bar &amp; Grill</div>
      <div class="order">ORDER DELIVERY<br>WWW.RUSTYLANTERNGRILL.COM<br><span class="phone">555-014-7720</span></div>
    </div>
    <div class="art art--diners" role="img" aria-label="Colourful painted illustration of cartoon animals sharing burgers and drinks at a table"></div>
  </div>
</section>

<section class="sheet sheet--inside">
  <div class="panel panel--grey">
    <div class="frame">
      <h2>STARTERS</h2>
      <div class="group">
        <h3>TORTILLA CHIPS:</h3>
        <div class="row">with House-made Salsa Verde<span class="dots"></span>7</div>
        <div class="row">with House-made Fire Roasted Salsa<span class="dots"></span>7</div>
        <div class="row">with Guacamole &amp; Pico De Gallo<span class="dots"></span>8</div>
        <div class="row">with Queso<span class="dots"></span>8</div>
        <div class="row">with Chili con Queso<span class="dots"></span>9</div>
      </div>
      <div class="group">
        <h3>WINGS:</h3>
        <div class="row">8 pieces<span class="dots"></span>14</div>
        <p class="desc">Flash-fried to a crispy golden brown and tossed in your choice of sauce. Choose from our Signature Hot, or Mild Sauce, or BBQ. Your choice of ranch or blue cheese.</p>
      </div>
      <div class="group">
        <h3>QUESADILLAS:</h3>
        <div class="row">Cheddar and Monterey Jack Cheese<span class="dots"></span>12</div>
        <div class="row">Pulled Marinated Chicken &amp; Cheese<span class="dots"></span>16</div>
        <div class="row">Fire Roasted Vegetables &amp; Cheese<span class="dots"></span>14</div>
        <div class="row">Garlic Roasted Shrimp &amp; Cheese<span class="dots"></span>16</div>
        <p class="desc">All quesadillas are stuffed with roasted red peppers, black beans and your choice below. Served with guacamole, pico de gallo, and chipotle crema on the side.</p>
      </div>
      <div class="group">
        <h3>LOADED LANTERN NACHOS:</h3>
        <p class="desc">Tortilla chips, melted white queso, Cheddar and Monterey Jack cheeses, pico de gallo, guacamole, chipotle sour cream, jalapenos, black beans, &amp; green onions</p>
        <div class="row">Rusty Lantern Chili Nachos<span class="dots"></span>14</div>
        <div class="row">Pulled Chicken Nachos<span class="dots"></span>16</div>
        <div class="row">Garlic Roasted Shrimp<span class="dots"></span>16</div>
        <div class="row">Fire Roasted Vegetables Nachos<span class="dots"></span>14</div>
        <p class="desc">Portobello, Red Peppers, &amp; Zucchini</p>
      </div>
      <div class="group">
        <h3>FRENCH FRIES:</h3>
        <p class="desc">Served with our house made Garlic Aioli and Spicy Ketchup.</p>
        <div class="row">Fries Only<span class="dots"></span>7</div>
        <div class="row">Sweet Potato Fries<span class="dots"></span>7</div>
        <div class="row">Cheddar-Jack Cheese Fries<span class="dots"></span>8</div>
        <div class="row">Cheddar-Jack Cheese, Bacon Fries<span class="dots"></span>9</div>
        <div class="row">Chili Cheese Fries<span class="dots"></span>10</div>
        <p class="desc">Topped with Rusty Lantern Chili, cheddar jack cheese and served with chipotle crema on the side.</p>
      </div>
    </div>
  </div>

  <div class="panel">
    <div class="tiny-logo">Rusty Lantern<small>Bar &amp; Grill</small></div>
    <h2 class="center" style="margin-top:8px">GOURMET BURGERS &amp; SANDWICHES</h2>
    <p class="intro">Start with your style and then choose your protein. Our burgers are house made and cooked to your temperature. Our fresh grilled chicken breast is marinated in house and cooked to perfection. Keep it vegetarian by choosing a vegetarian style along with the Quinoa Lentil Burger. All are served on a potato bun with lettuce, tomato, onion, and your choice of hand cut fries or sweet potato fries.<br><b style="color:var(--ink)">Premium sides available for an up charge + $2</b></p>
    <div class="rule"></div>
    <table class="burgers">
      <tr><th>Gluten-Free Bun Available Upon Request | $2</th><th><span class="icon"></span></th><th><span class="icon"></span></th><th><span class="icon"></span></th></tr>
      <tr><td><div class="name">The Copper</div><div class="desc">Roasted red peppers, red onions, brie cheese, and horseradish aioli.</div></td><td class="price">15.00*</td><td class="price">14.00</td><td class="price">13.00</td></tr>
      <tr><td><div class="name">The Ember</div><div class="desc">Cheddar, Monterey Jack, and Provolone</div></td><td class="price">15.00*</td><td class="price">14.00</td><td class="price">13.00</td></tr>
      <tr><td><div class="name">Spark Plug</div><div class="desc">Guacamole, 3 pepper colby jack, pico de gallo, and chipotle mayo.</div></td><td class="price">15.50*</td><td class="price">14.50</td><td class="price">13.50</td></tr>
      <tr><td><div class="name">The Big Flame</div><div class="desc">Fried egg*, bacon, cheddar cheese, and garlic aioli.</div></td><td class="price">16.00*</td><td class="price">15.00</td><td class="price">14.00</td></tr>
      <tr><td><div class="name">The Orchard</div><div class="desc">Melted brie cheese, sliced apple, and citrus aioli.</div></td><td class="price">16.50*</td><td class="price">15.50</td><td class="price">14.50</td></tr>
      <tr><td><div class="name">The Forager</div><div class="desc">Portobello mushrooms, roasted red peppers, smoked gouda cheese, and roasted garlic aioli.</div></td><td class="price">16.50*</td><td class="price">15.50</td><td class="price">14.50</td></tr>
      <tr><td><div class="name">The Harbor</div><div class="desc">Grilled shrimp*, roasted corn, swiss cheese, and roasted garlic aioli.</div></td><td class="price">16.50*</td><td class="price">15.50</td><td class="price">14.50</td></tr>
      <tr><td><div class="name">Build Your Own</div><div class="desc">Make it yours! Choose a cheese, condiment and one topping. Additional Toppings $1 | Bacon, Egg, Shrimp – $2</div></td><td class="price">14.00*</td><td class="price">13.00</td><td class="price">12.00</td></tr>
    </table>
  </div>

  <div class="panel">
    <div class="frame" style="margin:10px 6px 0">
      <div class="box-title">KIDS MENU:</div>
      <p class="note">All served with French Fries</p>
      <div class="row">Grilled Cheese<span class="dots"></span>8</div>
      <div class="row">Cheese Quesadilla<span class="dots"></span>8</div>
      <div class="row">Mac &amp; Cheese<span class="dots"></span>8</div>
      <div class="row">Chicken Tenders<span class="dots"></span>10</div>
    </div>
    <div class="rule" style="margin:8px 14px"></div>
    <div class="frame" style="margin:6px 6px 0;text-align:center">
      <div class="box-title">SIDES:</div>
      <p style="font-size:7px;margin-top:5px;line-height:1.5">Potato Salad $4 | Fire Roasted Veggies $6<br>Brown Rice, Quinoa, &amp; Kale Medley $5</p>
    </div>
    <div class="rule" style="margin:8px 14px"></div>
    <div class="frame" style="margin-top:8px;padding:6px 8px">
      <div class="box-title">OTHER HANDHELDS:</div>
      <p class="desc center">All served with Hand Cut Fries or Sweet Potato Fries. Premium sides available for an up charge +2</p>
      <div class="handhelds">
        <div class="hh-item"><div class="name"><span>Lantern Club</span><span>15</span></div><p class="desc">Sliced whole wheat bread with roasted garlic aioli, grilled marinated chicken breast, provolone cheese bacon, lettuce and tomato.</p></div>
        <div class="hh-item"><div class="name"><span>What's Gouda?</span><span>14</span></div><p class="desc">Sliced whole wheat bread with roasted garlic aioli smoked gouda and provolone cheeses, roasted red peppers and portobello mushrooms.</p></div>
        <div class="hh-item"><div class="name"><span>Southwest Melt</span><span>14</span></div><p class="desc">Sliced whole wheat bread with roasted garlic aioli, 3 pepper colby jack, roasted red peppers and corn.</p></div>
        <div class="hh-item"><div class="name"><span>Garden Melt</span><span>14</span></div><p class="desc">Sliced whole wheat bread with roasted garlic aioli, zucchini, portobello, mushrooms, red peppers, with melted brie and provolone cheeses.</p></div>
      </div>
    </div>
    <div class="extras">
      <div><h4>CHEESES:</h4><p>Vermont Cheddar | Smoked Gouda | 3-Pepper Colby Jack Monterey Jack | Swiss | Brie | Provolone | American.</p></div>
      <div><h4>CONDIMENTS:</h4><p>Horseradish Aioli | Chipotle Crema | Roasted Garlic Aioli | Citrus Aioli | Spicy Ketchup | Dijon Mustard | Yellow Mustard | Mayo | Ketchup</p></div>
      <div><h4>TOPPINGS:</h4><p>Bacon | Shrimp | Egg | Red Onion | White Onion | Portobello Mushrooms | Roasted Corn | Roasted Red Peppers | Guacamole | Pico De Gallo | Fresh or Pickled Jalapenos</p></div>
    </div>
  </div>
</section>

</body>
</html>
```